Luxury packaging graphic design for a new Hair care elixir

We need a packaging design for a new product for our line extension of hair colouring. We have already a packaging that is very well received (all in pink) including all accesories and transport box (attached files).
For a new product - protein for the hair - we need a different design tapping into luxury segment.

Target Market(s)

This product is mainly for women between 25-65 that are looking forward to improve hair strukture and make hair looks better, nicer, softer, healthier. The product in the packaging could be used up to 2x times.

Industry/Entity Type

Hair And Beauty

Font styles to use
Serif
Sans Serif

Colors

Designer to choose colors to be used in the design.

Requirements
Must have
• The material of the packaging are carton/styropor/and glass (attached a picture of packaging design to be adapted). The components are quite small so the packaging plays a big role to increase the value of what it is inside. The packaging needs to be inline with our actual packaging designs and corporate identity as they may be delivered together so as an assamble it should look nice, beautiful and of high quality.
• The graphic design for the different components to be adapted are:
• - grapich design for outside box
• - graphic design for the inside bottles
• - graphic design for the flyer/instructions inside the box
Nice to have
• It needs to feel that the packaging is Wow! It is going to be delivered per post so there have to be a beautiful opening effect. Eventually to work with colours like black, white and gold would give a nice luxury feeling.
• The actual product inside is a concentrated protein component so it is very small, therefore the packaging should show that even if small it is an elixir for the hair.
Should not have
• a totally diffenet look as our actual designs.

```html
<!DOCTYPE html>
<html lang="en">
<head>
<meta charset="utf-8">
<title>Noa Vell – Amber essence carton front</title>
<link href="https://fonts.googleapis.com/css2?family=Montserrat:wght@300;400&family=Arimo:wght@400&display=swap" rel="stylesheet">
<style>
  :root {
    --backdrop: #b3a193;
    --carton: #ffffff;
    --apricot: #e9a468;
    --ink: #1c1c1c;
    --gold-dark: #a8662a;
    --gold-mid: #e8a850;
    --gold-light: #f7ee9c;
  }
  html, body {
    margin: 0;
    padding: 0;
    width: 1140px;
    height: 1200px;
    overflow: hidden;
    background: var(--backdrop);
  }
  .carton-front {
    position: absolute;
    left: 373px;
    top: 50px;
    width: 394px;
    height: 1100px;
    background: var(--carton);
  }
  .centered {
    position: absolute;
    left: 0;
    width: 100%;
    text-align: center;
    transform: translateY(-50%);
  }
  .brand-name {
    top: 108px;
    font-family: "Montserrat", sans-serif;
    font-weight: 400;
    font-size: 46px;
    line-height: 1;
    color: var(--apricot);
    letter-spacing: 3px;
  }
  .tagline {
    top: 160px;
    font-family: "Montserrat", sans-serif;
    font-weight: 400;
    font-size: 15px;
    letter-spacing: 3.5px;
    color: var(--ink);
  }
  .gold-band {
    position: absolute;
    left: 0;
    top: 200px;
    width: 394px;
    height: 13px;
    background: linear-gradient(90deg, var(--gold-dark) 0%, var(--gold-mid) 35%, var(--gold-light) 90%, var(--gold-mid) 100%);
  }
  .emblem-area {
    position: absolute;
    left: 113px;
    top: 272px;
    width: 168px;
    height: 168px;
    border-radius: 50%;
    background: radial-gradient(circle at 40% 40%, #f8dcc2, #f1c094);
  }
  .product-name {
    top: 471px;
    font-family: "Montserrat", sans-serif;
    font-size: 30px;
    color: var(--apricot);
    line-height: 1;
  }
  .product-name .light { font-weight: 300; }
  .product-name .regular { font-weight: 400; }
  .language-label {
    font-family: "Arimo", sans-serif;
    font-size: 16px;
    line-height: 20px;
    letter-spacing: 1.2px;
    color: var(--ink);
  }
  .label-de { top: 818px; }
  .label-fr { top: 904px; }
  .label-en { top: 988px; }
  .divider {
    position: absolute;
    left: 0;
    width: 394px;
    height: 3px;
    background: var(--apricot);
  }
  .divider-1 { top: 854px; }
  .divider-2 { top: 946px; }
  .divider-3 { top: 1025px; }
  .volume {
    top: 1067px;
    font-family: "Arimo", sans-serif;
    font-size: 17px;
    letter-spacing: 1px;
    color: var(--ink);
  }
  .volume .estimated { font-size: 24px; vertical-align: -2px; }
</style>
</head>
<body>
  <main class="carton-front">
    <div class="centered brand-name">NOA VELL</div>
    <div class="centered tagline">A SHADE ALL YOUR OWN</div>
    <div class="gold-band"></div>

    <div class="emblem-area" role="img" aria-label="Line-drawn product emblem in apricot"></div>
    <div class="centered product-name"><span class="regular">Amber</span> <span class="light">essence</span></div>

    <div class="centered language-label label-de">STRAHLENDE FÄRBENDE<br>BEHANDLUNG</div>
    <div class="divider divider-1"></div>
    <div class="centered language-label label-fr">TRAITEMENT DE<br>COLORATION ÉCLANTE</div>
    <div class="divider divider-2"></div>
    <div class="centered language-label label-en">RADIANT COLORING<br>TREATMENT</div>
    <div class="divider divider-3"></div>

    <div class="centered volume">1:1 60ML <span class="estimated">℮</span></div>
  </main>
</body>
</html>
```